Harbinger Noble Alloys Works Business Cards

We are wanting to have a new business card designed for our company as we go to a convention. We want to balance business/Modern with elegance and beauty. Our company sells highend jewelry pieces. We want to utilize the colors of Black and Gold and have gold foiled fonts to be physically printed on the business cards.
We also would like to have space to write notes on the back side of the business card. When we meet people at jewelry conventions we would like to write notes if possible.
Here are websites and designs that we like the look and feel of these companies and you can use these as design ideas.
https://www.lorvanne.com
https://www.bellquist.com/en-us/home
Here is our company website link
www.harbingernaw.com
I also up loaded two versions of our logo.
- Update 4.26.22
I have uploaded photos of a business card we like. this card has raised embossed letters that you can feel. the raise letters are like a plastic but we don't need to use that...I uploaded to show you that we like the experience of the client feeling the characters of the logo. we also would like to have the material as a satin or some material very soft.
- Maybe we can get designs with beautiful gold foiling and raised characters and logos. we like simplicity...not busy but an elegant design. We need to write notes and would like a section where we can write notes. but we want an elegant style and the client has an experience with the feel of the card when they touch the card.
Colors
- Main colors Black & Gold
- white or light colors for small notes section.
Specialty ideals and things we would like to see based on your design styles.
- raised fonts
- raised logos
- gold foiling
- satin/soft finish on the card material.
we are wanting to design a business card that looks elegant and clean. When the client is handed the business card we want them to physically experience the business card as well by touching the raised logos or fonts and the base material is soft satin. I hope this helps with further designs.
thank you all
We uploaded a new contact layout that we have designed in our office. we would like to see how this would look on your designs.
thank you
I just finished uploading the Contact Layout. the colors are just examples. please use this layout as an idea and use colors based on the feed back we have given each of you personally.
Contact Information for Business Card
we need an area to write notes, we would like to have our logos or the diamond of our logo or the business card to have embossed sections to the business card so when the customer touches the card they can feel the logo. we would also like sections of our business card to have gold foiling. we would also like to use a satin soft paper with our card. when the client touches the card its super soft and high quality
Requirements
Must have
- we would like to have our logos or the diamond of our logo or the business card to have embossed sections to the business card so when the customer touches the card they can feel the logo. we would also like sections of our business card to have gold foiling. we would also like to use a satin soft paper with our card. when the client touches the card its super soft and high quality
Nice to have
- we would like to have our logos or the diamond of our logo or the business card to have embossed sections to the business card so when the customer touches the card they can feel the logo. we would also like sections of our business card to have gold foiling.

```html
<!DOCTYPE html>
<html lang="en">
<head>
<meta charset="utf-8">
<title>Harbinger Noble Alloys Works — Business Cards</title>
<link rel="stylesheet" href="https://fonts.googleapis.com/css2?family=Cormorant+SC:wght@500;600&family=Lato:ital,wght@0,400;1,400&display=swap">
<style>
  :root {
    --canvas: #161616;
    --card-dark: #2e2a2c;
    --card-dark-edge: #242123;
    --gold: #c9a54e;
    --gold-light: #e3c77c;
    --ink-light: #f4f2ef;
    --muted: #9b979a;
    --band-grey: #6c6d70;
    --paper: #f3f3f3;
    --rule: #2a2a2a;
  }
  * { box-sizing: border-box; margin: 0; padding: 0; }
  html, body { width: 1200px; height: 1200px; overflow: hidden; }
  body { background: var(--canvas); position: relative; font-family: "Lato", sans-serif; }

  .card {
    position: absolute;
    width: 502px;
    height: 288px;
    overflow: hidden;
  }

  /* Front */
  .card-front {
    left: 80px; top: 438px;
    background: linear-gradient(160deg, var(--card-dark), var(--card-dark-edge));
  }
  .front-frame {
    position: absolute;
    left: 17px; top: 21px; right: 19px; bottom: 17px;
    border: 3px solid var(--gold);
  }
  .brand-name {
    position: absolute;
    left: 0; right: 0; top: 124px;
    text-align: center;
    font-family: "Cormorant SC", serif;
    font-weight: 600;
    font-size: 28px;
    letter-spacing: 0.5px;
    color: var(--ink-light);
  }
  .brand-tagline {
    position: absolute;
    left: 0; right: 0; top: 157px;
    text-align: center;
    font-family: "Cormorant SC", serif;
    font-weight: 600;
    font-size: 20px;
    letter-spacing: 0.4px;
    color: var(--ink-light);
  }
  .front-ornament {
    position: absolute;
    left: 231px; top: 208px;
    width: 40px; height: 28px;
    border-radius: 6px;
    background: radial-gradient(ellipse at center, rgba(240,238,235,0.35), rgba(240,238,235,0));
  }

  /* Back */
  .card-back {
    left: 629px; top: 437px;
    background: var(--card-dark);
  }
  .back-shapes { position: absolute; inset: 0; }
  .back-brand {
    position: absolute;
    left: 42px; top: 40px;
    font-family: "Lato", sans-serif;
    font-size: 13px;
    letter-spacing: 0.3px;
    color: var(--gold);
  }
  .employee-name {
    position: absolute;
    left: 48px; top: 74px;
    font-size: 23px;
    color: var(--ink-light);
    letter-spacing: 0.2px;
  }
  .employee-title {
    position: absolute;
    left: 48px; top: 105px;
    font-size: 13px;
    font-style: italic;
    color: var(--muted);
  }
  .contact {
    position: absolute;
    left: 48px; top: 152px;
    font-size: 13.5px;
    line-height: 17px;
    color: var(--ink-light);
    list-style: none;
  }
  .contact li + li.gap { margin-top: 4px; }
  .contact li.gap-lg { margin-top: 9px; }
</style>
</head>
<body>

  <section class="card card-front" aria-label="Business card front">
    <div class="front-frame"></div>
    <h1 class="brand-name">Harbinger Noble Alloys</h1>
    <p class="brand-tagline">– Coins, Jewelry &amp; Diamonds –</p>
    <div class="front-ornament" role="img" aria-label="Small ornamental flourish"></div>
  </section>

  <section class="card card-back" aria-label="Business card back">
    <svg class="back-shapes" width="502" height="288" viewBox="0 0 502 288" aria-hidden="true">
      <path d="M279,0 C262,90 268,170 289,288 L502,288 L502,0 Z" fill="var(--band-grey)"/>
      <path d="M287,0 C270,90 276,170 297,288 L502,288 L502,0 Z" fill="var(--paper)"/>
      <polyline points="299,18 486,18 486,269 302,269" fill="none" stroke="var(--rule)" stroke-width="1.6"/>
      <rect x="462" y="34" width="11" height="11" fill="var(--muted)"/>
      <rect x="462" y="242" width="11" height="11" fill="var(--muted)"/>
      <text x="470" y="144" transform="rotate(90 470 144)" text-anchor="middle"
            font-family="Cormorant SC, serif" font-weight="600" font-size="15"
            letter-spacing="0.5" fill="var(--band-grey)">Note</text>
    </svg>

    <p class="back-brand">Harbinger Noble Alloys</p>
    <h2 class="employee-name">Employee Name</h2>
    <p class="employee-title">Title/ Position</p>
    <ul class="contact">
      <li>TEL: 555.014.2760</li>
      <li class="gap">2210 Larkmoor Ave NE</li>
      <li>Fenwick, OR 97000</li>
      <li class="gap-lg">hello@harbingernaw.com</li>
      <li>www.harbingernaw.com</li>
    </ul>
  </section>

</body>
</html>
```